Martin & Ilse Crowther
WE HAVE MOVED
The address of our new home is
Fern Hollow
48 Wexcombe Lane
Thornby on Wyle
Warwickshire
B97 3LT
Tel: 07912 408716
Email: martin@kelvo.uk.com

```html
<!DOCTYPE html>
<html lang="en">
<head>
<meta charset="utf-8">
<title>We Have Moved – Martin &amp; Ilse Crowther</title>
<link rel="stylesheet" href="https://fonts.googleapis.com/css2?family=Sacramento&family=Open+Sans:wght@400&family=Cormorant+Garamond:wght@500&display=swap">
<style>
  :root {
    --paper: #ffffff;
    --ink: #2c2c2e;
    --script-green: #2f6a3a;
    --leaf-deep: #1f8a6a;
    --leaf-mid: #6fa64a;
    --leaf-light: #b9d58f;
  }
  * { margin: 0; padding: 0; box-sizing: border-box; }
  html, body {
    width: 1200px;
    height: 852px;
    overflow: hidden;
    background: var(--paper);
  }
  .card {
    position: relative;
    width: 1200px;
    height: 852px;
    background: var(--paper);
    overflow: hidden;
  }
  .foliage {
    position: absolute;
    border-radius: 50%;
    opacity: 0.85;
  }
  .foliage--top-right {
    top: -60px;
    right: -40px;
    width: 270px;
    height: 270px;
    background: radial-gradient(circle at 55% 40%, var(--leaf-deep) 0%, var(--leaf-mid) 45%, rgba(185,213,143,0.5) 68%, rgba(255,255,255,0) 72%);
  }
  .foliage--bottom-left {
    left: -70px;
    bottom: -60px;
    width: 330px;
    height: 430px;
    background: radial-gradient(ellipse at 40% 55%, var(--leaf-mid) 0%, var(--leaf-deep) 38%, rgba(185,213,143,0.5) 66%, rgba(255,255,255,0) 71%);
  }
  .foliage--bottom-right {
    right: -40px;
    bottom: -70px;
    width: 260px;
    height: 250px;
    background: radial-gradient(circle at 50% 50%, var(--leaf-deep) 0%, var(--leaf-mid) 42%, rgba(185,213,143,0.5) 66%, rgba(255,255,255,0) 71%);
  }
  .foliage--edge-right {
    right: -20px;
    top: 505px;
    width: 36px;
    height: 110px;
    background: radial-gradient(ellipse at 70% 50%, var(--leaf-deep) 0%, rgba(31,138,106,0.4) 55%, rgba(255,255,255,0) 70%);
  }
  .announcement {
    position: absolute;
    right: 179px;
    top: 120px;
    text-align: right;
  }
  .announcement__title {
    font-family: "Sacramento", cursive;
    font-weight: 400;
    font-size: 96px;
    line-height: 1;
    color: var(--script-green);
    margin-bottom: 42px;
  }
  .address {
    font-family: "Open Sans", sans-serif;
    font-style: normal;
    font-size: 29px;
    line-height: 57px;
    letter-spacing: 0.09em;
    color: var(--ink);
  }
  .address__line { display: block; }
  .signature {
    font-family: "Cormorant Garamond", serif;
    font-weight: 500;
    font-size: 35px;
    letter-spacing: 0.06em;
    color: var(--ink);
    margin-top: 40px;
  }
</style>
</head>
<body>
  <main class="card">
    <div class="foliage foliage--top-right" role="img" aria-label="Watercolour green leafy sprigs in the top right corner"></div>
    <div class="foliage foliage--bottom-left" role="img" aria-label="Watercolour green leafy branches in the bottom left corner"></div>
    <div class="foliage foliage--bottom-right" role="img" aria-label="Watercolour green leafy sprigs in the bottom right corner"></div>
    <div class="foliage foliage--edge-right" role="img" aria-label="Tip of a green leaf sprig at the right edge"></div>

    <section class="announcement">
      <h1 class="announcement__title">We Have Moved!</h1>
      <address class="address">
        <span class="address__line">OUR NEW ADDRESS:</span>
        <span class="address__line">Fern Hollow,48 Wexcombe Lane,</span>
        <span class="address__line">Thornby on Wyle,Warwickshire, B97 3LT.</span>
        <span class="address__line">Tel: 07912 408716</span>
        <span class="address__line">Email: martin@kelvo.uk.com</span>
      </address>
      <p class="signature">WITH LOVE Martin &amp; Ilse Crowther</p>
    </section>
  </main>
</body>
</html>
```